Corbin Lantern Lighting - Commercial & Residential Landscape Lighting

Landscape Lighting Services & Design: Create a website for our landscape lighting company. We would like the design to be tailored around this description:
Illuminate with Confidence. Designed with Precision. Installed with Care.
Locally and veteran-owned, we take pride in transforming outdoor spaces through innovative lighting solutions tailored to your vision. From landscape and holiday lighting to permanent installations, our effortless process and expert design deliver breathtaking results and lasting curb appeal. Backed by a lifetime warranty and quarterly service options, our commitment to quality and customer satisfaction is unwavering. Try before you buy and experience your home in a whole new light with our complimentary demo kit — see the stunning effects before you decide.
- Also, add in this information as well; Outdoor Lighting not only beautifies spaces but also significantly enhances safety by illuminating your home or business. Beautifully lit entrances deter potential intruders, making your home a safer place for your loved ones. we also offer quarterly service plans to ensure lighting equipment continues to operate & illuminate effectively throughout the year. Also mention we provide free estimates and we are offering a 10% discount to military, veterans, and first responders.

Target Market(s)

Luxury market

Industry/Entity Type

Landscape Lighting - Residential & Commercial Lighting Services

Coding

Coded - Design and coding required

Number of Pages Required

2 page

Colors
00AB8E
00BBA5
67D7C9
C6EFE9
E9F9F6
59FF00
82FF00
B8FF75
E3FFCB
F4FFEA
FFC000
F8CF3A
FAE287
FDF2CF
FEFAEE

Requirements
Must have
• a lead generation button where people can submit their information for us to reach out to them and schedule their free estimate, homepage, about page, contact page, products and services page, user friendly, easy to navigate, and it also must be engaging and eye popping, as well as appealing to the luxury market. Please use colors; verdent green, dark green, ivory, and sunny yellow. Also, include an about page that references our story; Derek is retired Army and he opened a fitness studio in 2017 with his wife Vanessa. He has installed low voltage lighting in every home he lived in and for his friends and family over the years and decided to open his own business because he is passionate about beautifying outdoor landscapes and highlighting a properties full potential, not only in the day but at night as well all while providing safety and security for his clients. Having a deep respect for nature and landscaping, he wants to provide the same care and quality to each of his clients as he has in the fitness industry for decades. He believes small businesses are the back bone of America and he's excited to provide a service that is all to often neglected in the design of a home.
Nice to have
• I would like to have a clear intent and purpose, engaging web design, clear call to action, optimized for search engines, mobile friendy design, security measures, credibility indicators

```html
<!DOCTYPE html>
<html lang="en">
<head>
<meta charset="utf-8">
<title>Gallery | Corbin Lantern Lighting</title>
<link href="https://fonts.googleapis.com/css2?family=Josefin+Sans:wght@300;400;600;700&family=Montserrat:wght@600;700&display=swap" rel="stylesheet">
<style>
:root{
  --deep-green:#04140e;
  --forest:#0a2419;
  --moss:#123527;
  --verdant:#00ab8e;
  --verdant-soft:#67d7c9;
  --sun:#ffc000;
  --sun-warm:#f8cf3a;
  --sun-pale:#fae287;
  --ivory:#fefaee;
  --ivory-dim:#fdf2cf;
  --line:rgba(254,250,238,.22);
  --bar:#02100a;
}
*{margin:0;padding:0;box-sizing:border-box}
html,body{width:1200px;height:2679px;overflow:hidden;background:var(--deep-green)}
body{position:relative;font-family:"Josefin Sans",sans-serif;color:var(--ivory)}
a{text-decoration:none}
.abs{position:absolute}
.hero{left:0;top:0;width:1200px;height:545px;background:linear-gradient(180deg,#0c1f14 0%,#14301f 35%,#1d3a2c 60%,#2c4a44 85%,#23403a 100%)}
.hero-curve{left:0;top:420px}
.nav-line{left:85px;width:1080px;height:1px;background:var(--line)}
.top-nav a{position:absolute;top:61px;font-size:15px;color:var(--sun-pale);letter-spacing:.3px}
.top-nav a.active{color:var(--sun)}
.active-bar{left:770px;top:102px;width:50px;height:2px;background:var(--sun)}
.brand{text-align:center;color:var(--sun-warm);font-weight:300;line-height:1}
.brand .big{display:block;font-size:44px;letter-spacing:2px}
.brand .small{display:block;font-size:12px;letter-spacing:3.5px;margin-top:6px}
.cta{left:1018px;top:47px;width:153px;height:40px;border-radius:20px;background:var(--sun);color:var(--deep-green);font-family:Montserrat,sans-serif;font-weight:700;font-size:12px;display:flex;align-items:center;justify-content:center;letter-spacing:.3px}
.title{left:0;width:1200px;text-align:center;color:var(--sun-warm);font-weight:600;letter-spacing:1px}
.rule{height:2px;background:linear-gradient(90deg,transparent,var(--sun) 30%,var(--sun) 70%,transparent)}
.eyebrow{left:0;top:536px;width:1200px;text-align:center;font-size:16px;letter-spacing:4px;color:var(--verdant-soft)}
.intro{left:195px;width:810px;text-align:center;font-size:17px;line-height:27px;color:var(--ivory)}
.intro p{margin-bottom:12px}
.tagline{left:0;top:862px;width:1200px;text-align:center;color:var(--sun);font-weight:700;font-size:22px}
.sub{left:0;top:904px;width:1200px;text-align:center;font-size:17px;color:var(--ivory-dim)}
.tile{width:323px;height:231px}
.videos-bg{left:0;top:1740px;width:1200px;height:670px;background:radial-gradient(ellipse at 50% 60%,#163a2a 0%,#0a2419 55%,#04140e 100%)}
.video{height:335px}
.play{left:50%;top:50%;width:54px;height:54px;margin:-27px 0 0 -27px}
.footer-nav a{position:absolute;top:2452px;font-family:Montserrat,sans-serif;font-weight:700;font-size:13.5px;color:var(--ivory)}
.dot{width:4px;height:4px;background:var(--sun)}
.contact{top:2540px;display:flex;align-items:center;gap:12px;font-family:Montserrat,sans-serif;font-weight:600;font-size:13px;color:var(--ivory)}
.contact .ic{width:35px;height:35px;border-radius:50%;background:var(--verdant);display:flex;align-items:center;justify-content:center}
.social{top:2546px;width:27px;height:27px;border-radius:50%;background:var(--sun)}
.copy{left:0;top:2628px;width:1200px;height:51px;background:var(--bar);color:var(--ivory-dim);font-size:14px;display:flex;align-items:center;justify-content:center}
</style>
</head>
<body>

<div class="abs hero" role="img" aria-label="Night photo of a lit hedge above a paver walkway"></div>
<svg class="abs hero-curve" width="1200" height="130" viewBox="0 0 1200 130">
  <path d="M0 125 L0 92 Q600 -20 1200 110 L1200 130 Z" fill="#04140e"/>
  <path d="M120 85 Q600 -15 1168 100" fill="none" stroke="#ffc000" stroke-width="3"/>
</svg>

<header>
  <div class="abs nav-line" style="top:33px"></div>
  <div class="abs nav-line" style="top:104px"></div>
  <nav class="top-nav">
    <a href="#" style="left:141px">HOME</a>
    <a href="#" style="left:236px">ABOUT</a>
    <a href="#" style="left:338px">SERVICES</a>
    <a href="#" class="active" style="left:765px">GALLERY</a>
    <a href="#" style="left:880px">CONTACT US</a>
  </nav>
  <div class="abs active-bar"></div>
  <div class="abs brand" style="left:480px;top:38px;width:240px">
    <span class="big">CORBIN</span>
    <span class="small">LANTERN LIGHTING</span>
  </div>
  <a class="abs cta" href="#">FREE ESTIMATE &rsaquo;</a>
</header>

<h1 class="abs title" style="top:205px;font-size:41px">OUR GALLERY</h1>
<div class="abs rule" style="left:452px;top:261px;width:305px"></div>

<section>
  <div class="abs eyebrow">SEE OUR WORK</div>
  <h2 class="abs title" style="top:564px;font-size:38px">SEE THE DIFFERENCE. FEEL THE IMPACT</h2>
  <div class="abs rule" style="left:455px;top:616px;width:310px"></div>
  <div class="abs intro" style="top:638px">
    <p>Welcome to the Corbin Lantern Lighting Gallery — where ordinary spaces are transformed into extraordinary showcases of light, elegance, and design.</p>
    <p>Every image you see here is more than just a project — it's a custom-tailored lighting experience, thoughtfully engineered to elevate curb appeal, highlight architectural beauty, and create unforgettable ambiance.</p>
    <p>Our work speaks louder than words — because when the sun sets, excellence should rise.</p>
  </div>
  <div class="abs tagline">Browse. Dream. Be Inspired.</div>
  <div class="abs sub">Then let us bring your vision to life, one perfectly placed light at a time.</div>

  <div class="abs tile" style="left:107px;top:979px;background:linear-gradient(135deg,#6b4a28,#2a1c10)" role="img" aria-label="Uplight washing a stucco pillar"></div>
  <div class="abs tile" style="left:450px;top:979px;background:linear-gradient(135deg,#3a3a30,#1a2418)" role="img" aria-label="Lit home entrance with palms"></div>
  <div class="abs tile" style="left:792px;top:979px;background:linear-gradient(160deg,#1d2a44,#2c2a1c)" role="img" aria-label="Stone path with path lights"></div>
  <div class="abs tile" style="left:107px;top:1235px;background:linear-gradient(160deg,#3a3a34,#4a6a2a)" role="img" aria-label="Patio slab beside lit shrub"></div>
  <div class="abs tile" style="left:450px;top:1235px;background:linear-gradient(180deg,#0a1428,#3a3020 55%,#2a4018)" role="img" aria-label="Brick house front lit at night"></div>
  <div class="abs tile" style="left:792px;top:1235px;background:linear-gradient(180deg,#5a7090,#4a5a40 55%,#8a8a80)" role="img" aria-label="Two-storey house at dusk with landscaping"></div>
  <div class="abs tile" style="left:107px;top:1492px;background:linear-gradient(160deg,#2a4aa0,#6a5a20 60%,#2a4a18)" role="img" aria-label="Uplit crape myrtle trees at dusk"></div>
  <div class="abs tile" style="left:450px;top:1492px;background:linear-gradient(160deg,#2a3a20,#5a5a50 70%,#3a3a38)" role="img" aria-label="Lit tree by a courtyard fence"></div>
  <div class="abs tile" style="left:792px;top:1492px;background:linear-gradient(135deg,#4a4a44,#c8c4b8 55%,#2a3a20)" role="img" aria-label="Wall wash lighting on a siding wall"></div>
</section>

<section>
  <div class="abs videos-bg" role="img" aria-label="Evening backdrop of a lit garden and house"></div>
  <h2 class="abs title" style="top:1832px;font-size:41px">WATCH OUR VIDEOS</h2>
  <div class="abs rule" style="left:478px;top:1895px;width:310px"></div>

  <div class="abs video" style="left:124px;top:1950px;width:482px;background:linear-gradient(180deg,#2a2218,#7a6a48 55%,#2a2218)" role="img" aria-label="Video: step light on a wooden deck">
    <svg class="abs play" viewBox="0 0 54 54"><circle cx="27" cy="27" r="24" fill="none" stroke="#fefaee" stroke-width="4"/><path d="M21 16 L38 27 L21 38 Z" fill="#fefaee"/></svg>
  </div>
  <div class="abs video" style="left:627px;top:1952px;width:482px;background:linear-gradient(135deg,#6a6a20,#1e2a14 60%,#141a10)" role="img" aria-label="Video: spotlight among shrub leaves">
    <svg class="abs play" viewBox="0 0 54 54"><circle cx="27" cy="27" r="24" fill="none" stroke="#fefaee" stroke-width="4"/><path d="M21 16 L38 27 L21 38 Z" fill="#fefaee"/></svg>
  </div>
  <div class="abs" style="left:1110px;top:1940px;width:90px;height:345px;background:linear-gradient(180deg,#12261c,#5a4020)" role="img" aria-label="Next video preview"></div>
  <svg class="abs" style="left:78px;top:2078px" width="24" height="44" viewBox="0 0 24 44"><path d="M22 2 L3 22 L22 42" fill="none" stroke="#fefaee" stroke-width="3"/></svg>
  <svg class="abs" style="left:1135px;top:2078px" width="24" height="44" viewBox="0 0 24 44"><path d="M2 2 L21 22 L2 42" fill="none" stroke="#fefaee" stroke-width="3"/></svg>
</section>

<footer>
  <div class="abs nav-line" style="top:2418px;left:118px;width:970px"></div>
  <div class="abs nav-line" style="top:2505px;left:118px;width:970px"></div>
  <nav class="footer-nav">
    <a href="#" style="left:150px">HOME</a>
    <a href="#" style="left:263px">ABOUT US</a>
    <a href="#" style="left:407px">SERVICES</a>
    <a href="#" style="left:745px">PRODUCTS</a>
    <a href="#" style="left:894px">GALLERY</a>
    <a href="#" style="left:1024px">CONTACT</a>
  </nav>
  <div class="abs dot" style="left:234px;top:2459px"></div>
  <div class="abs dot" style="left:373px;top:2459px"></div>
  <div class="abs dot" style="left:855px;top:2459px"></div>
  <div class="abs dot" style="left:990px;top:2459px"></div>
  <div class="abs brand" style="left:497px;top:2440px;width:240px">
    <span class="big">CORBIN</span>
    <span class="small">LANTERN LIGHTING</span>
  </div>

  <div class="abs contact" style="left:143px">
    <span class="ic"><svg width="16" height="20" viewBox="0 0 16 20"><path d="M8 0C3.6 0 0 3.4 0 7.7 0 13 8 20 8 20s8-7 8-12.3C16 3.4 12.4 0 8 0z" fill="#fefaee"/><circle cx="8" cy="7.5" r="3" fill="#00ab8e"/></svg></span>
    123 Street Address line
  </div>
  <div class="abs contact" style="left:419px">
    <span class="ic"><svg width="18" height="18" viewBox="0 0 24 24"><path d="M6.6 10.8c1.4 2.8 3.8 5.1 6.6 6.6l2.2-2.2c.3-.3.7-.4 1-.2 1.1.4 2.3.6 3.6.6.6 0 1 .4 1 1V20c0 .6-.4 1-1 1C10.6 21 3 13.4 3 4c0-.6.4-1 1-1h3.5c.6 0 1 .4 1 1 0 1.3.2 2.5.6 3.6.1.3 0 .7-.2 1z" fill="#fefaee"/></svg></span>
    (555) 014-2287
  </div>
  <div class="abs contact" style="left:621px;gap:16px">
    <span class="ic"><svg width="18" height="14" viewBox="0 0 18 14"><rect width="18" height="14" rx="2" fill="#fefaee"/><path d="M1 1.5 L9 8 L17 1.5" fill="none" stroke="#00ab8e" stroke-width="1.6"/></svg></span>
    enquiry@corbinlantern.com
  </div>
  <div class="abs social" style="left:943px"></div>
  <div class="abs social" style="left:980px"></div>
  <div class="abs social" style="left:1019px"></div>
  <div class="abs social" style="left:1058px"></div>

  <div class="abs copy">Copyright © 2025 Corbin&nbsp;|&nbsp; All Right Reserved</div>
</footer>

</body>
</html>
```